WP website design Pardo-Kettleby(Contest)

We need a wordpress design that will incorporate a professional color scheme with company logo in a clean layout. The design needs to consider that this will be developed on a responsive theme. Colors are blue and green of the logo and and an accent color (perhaps very light brown/tan). Client wants a 'modern' look.

Industry/Entity Type

It Company

Font styles to use
Serif
Sans Serif

Colors

Designer to choose colors to be used in the design.

Requirements
Must have
• navigation: 1) Home; 2) Services; 3) Auctions by Type; 4) About Us; 5) VQL Digest 6) Videos; 7) Contact Us

VERY general idea of layout is attached, Site will have slideshow, image is attached. Widgets used to are: 1) Email Contact Form; 2) social media icons, FB LinedIn, YouTube; 3) Featured Auctions; 4) News & Events blog; Featured Video

Footer will have affiliation logos, contact info and perhaps smaller company logo:
Phone: (555) 304-7192 / Mobile: (555) 618-2047 (Mirna)
Email: mkettleby417@postvale.example / dennis@pardokettleby.example
Address: 415 FM 733N • #B207 • PMB318 • Austin, TX 78690

Nice to have
• Use of a dropdown menu

```html
<!DOCTYPE html>
<html lang="en">
<head>
<meta charset="utf-8">
<title>Pardo-Kettleby Auction Marketing</title>
<link href="https://fonts.googleapis.com/css2?family=Cabin:wght@400;500;600;700&family=Arimo:wght@400;700&display=swap" rel="stylesheet">
<style>
:root{
  --blue:#1a5fa3;
  --blue-deep:#0a4d8f;
  --green:#17875a;
  --green-deep:#0c6a43;
  --ink:#1f1f1f;
  --paper:#f0f0ee;
  --footer:#222222;
  --white:#ffffff;
}
*{margin:0;padding:0;box-sizing:border-box}
html,body{width:1092px;height:1200px;overflow:hidden}
body{position:relative;background:var(--paper);font-family:"Arimo",Arial,sans-serif;color:var(--ink)}
.site-header{position:absolute;left:0;top:0;width:1092px;height:149px;background:linear-gradient(#ffffff,#ececec);border-bottom:3px solid var(--blue-deep)}
.brand{position:absolute;left:91px;top:27px;width:218px;height:110px;background:linear-gradient(#ffffff,#f2f2f2);display:flex;flex-direction:column;align-items:center;justify-content:center;font-family:"Cabin",sans-serif;font-weight:700;color:var(--blue);text-align:center}
.brand .name{font-size:26px;line-height:1.1}
.brand .tag{font-size:19px;line-height:1.1;margin-top:4px}
.social{position:absolute;top:39px;left:636px;display:flex;gap:11px}
.social span{width:34px;height:34px;border-radius:50%;border:3px solid #cfcfcf}
.social .s1{background:#3b5a98}.social .s2{background:#e56a1f}.social .s3{background:#3ba6dd}
.contact{position:absolute;left:842px;top:41px;font-size:13px;line-height:20px;color:var(--blue-deep)}
.nav{position:absolute;left:380px;top:99px;display:flex;align-items:center;font-size:13px}
.nav a{color:var(--ink);text-decoration:none;padding:7px 0;margin-right:32px}
.nav a.active{background:var(--green);color:var(--white);padding:7px 14px;border-radius:2px;margin-right:18px}
.hero{position:absolute;left:0;top:149px;width:1092px;height:390px;background:linear-gradient(#4f8fd3 0%,#9cc2e6 38%,#6e7b5a 55%,#4e8a2f 75%,#3f7a24 100%)}
.hero-caption{position:absolute;left:491px;top:153px;width:510px;height:77px;background:rgba(18,90,170,.82);color:var(--white);font-family:"Cabin",sans-serif;font-weight:600;font-size:23px;line-height:32px;padding:7px 17px}
.btn{display:inline-block;background:linear-gradient(#ffffff,#d8d8d8);color:#2a2a2a;font-family:"Cabin",sans-serif;font-weight:500;border-radius:2px;text-align:center}
.hero-caption .btn{position:absolute;left:344px;top:20px;width:143px;height:36px;line-height:36px;font-size:22px}
.intro{position:absolute;left:0;top:556px;width:1092px;text-align:center;font-family:"Cabin",sans-serif;font-weight:500;font-size:22px;line-height:29px}
.rule{position:absolute;left:300px;width:492px;height:1px;background:linear-gradient(90deg,transparent,#a9a9a9,transparent)}
.upcoming{position:absolute;left:136px;top:679px;width:241px;height:328px;background:linear-gradient(#1768ac,#0b4f8e);color:var(--white);text-align:center;font-family:"Cabin",sans-serif}
.upcoming h2{font-weight:600;font-size:23px;margin-top:17px;text-align:left;padding-left:20px}
.upcoming .photo{width:193px;height:111px;margin:16px auto 0;border:2px solid #2a9a5c}
.upcoming p{font-size:11.5px;line-height:18px;margin:17px 18px 0}
.upcoming .btn{width:111px;height:29px;line-height:29px;font-size:17px;margin-top:14px}
.card{position:absolute;width:214px;height:152px;background:linear-gradient(var(--green),var(--green-deep));border-radius:3px;color:var(--white);font-family:"Cabin",sans-serif;font-weight:600;font-size:20px;letter-spacing:1px;text-align:center;line-height:21px}
.card .label{height:47px;display:flex;align-items:center;justify-content:center}
.card .photo{width:183px;height:94px;margin:0 auto;border:2px solid var(--white)}
.photo{background:linear-gradient(#7aa9dc 0%,#c9c2a8 45%,#8a7b5d 75%,#5f8a3d 100%)}
.photo.factory{background:linear-gradient(#c7cdd2,#4c8c6e 55%,#9aa0a4)}
.site-footer{position:absolute;left:0;top:1064px;width:1092px;height:136px;background:var(--footer);color:var(--white);font-size:13px;line-height:22px}
.site-footer .info{position:absolute;left:91px;top:20px}
.badges span{position:absolute;background:#9a9a9a}
</style>
</head>
<body>
<header class="site-header">
  <div class="brand"><span class="name">Pardo-Kettleby</span><span class="tag">Auction Marketing</span></div>
  <div class="social" aria-label="Social links"><span class="s1"></span><span class="s2"></span><span class="s3"></span></div>
  <div class="contact">Call Us: 1 800 555 0148<br>info@pardokettleby.com</div>
  <nav class="nav"><a class="active" href="#">Home</a><a href="#">Services</a><a href="#">Auctions by Type</a><a href="#">About Us</a><a href="#">VQL Digest</a><a href="#">Videos</a><a href="#">Contact Us</a></nav>
</header>
<section class="hero" role="img" aria-label="Large shingled estate home with chimneys, garden and lawn under blue sky">
  <div class="hero-caption">Making "SOLD" Our Specialty<br>for 30 Years<span class="btn">Read More</span></div>
</section>
<div class="rule" style="top:556px"></div>
<div class="intro" style="top:563px">The go-to business asset liquidation and real estate at auction solution provider in Texas<br>and across the southwest for over 30 years using our proprietary VQL process.</div>
<div class="rule" style="top:637px"></div>
<section class="upcoming">
  <h2>Upcoming Auction</h2>
  <div class="photo factory" role="img" aria-label="Machine shop floor with industrial equipment"></div>
  <p>simply dummy text of the printing and typesetting industry. Lorem Ipsum has been the industry's stan-dard dummy text ever since</p>
  <span class="btn">Read More</span>
</section>
<div class="card" style="left:458px;top:680px"><div class="label">REAL ESTATE</div><div class="photo" role="img" aria-label="Suburban two-storey house"></div></div>
<div class="card" style="left:722px;top:679px"><div class="label">BUSINESS<br>LIQUIDATION</div><div class="photo" role="img" aria-label="White house under blue sky"></div></div>
<div class="card" style="left:458px;top:858px"><div class="label">COMMERCIAL<br>ASSETS</div><div class="photo" role="img" aria-label="Stone-fronted family home"></div></div>
<div class="card" style="left:722px;top:858px"><div class="label">APPRAISALS</div><div class="photo" role="img" aria-label="Close view of house gables and windows"></div></div>
<footer class="site-footer">
  <div class="info">The VQL Digest: Dennis Kettleby Receives Lifetime Achievement Award Llinks to VQL Digest (former news)<br>Phone: (555) 304-7192 / Mobile: (555) 618-2047 (Mirna)<br>Email: mkettleby417@postvale.example / dennis@pardokettleby.example<br>Address: 415 FM 733N • #B207 • PMB318 • Austin, TX 78690</div>
  <div class="badges" aria-label="Affiliations">
    <span style="left:819px;top:16px;width:48px;height:48px;border-radius:50%"></span>
    <span style="left:889px;top:14px;width:44px;height:44px"></span>
    <span style="left:806px;top:71px;width:54px;height:46px"></span>
    <span style="left:869px;top:76px;width:96px;height:38px"></span>
  </div>
</footer>
</body>
</html>
```